Bright Hollow Syrup labels

Design for 3" round labels for 8 oz. maple syrup jars. Must include a picture (or outline) of an irish setter, a maple leaf (?) and the name "Bright Hollow Syrup" and the location Schoodic Lake, Maine. 8 fl oz (237 ml) and Grade A Amber. Here's my shitty stab at it. I want less leaf and more dog. I've included marginal pictures of the dog. I would prefer the dog center in the middle and the leaf behind it.

```html
<!DOCTYPE html>
<html lang="en">
<head>
<meta charset="utf-8">
<title>Bright Hollow Syrup – Maple Syrup Label</title>
<link rel="stylesheet" href="https://fonts.googleapis.com/css2?family=Lexend:wght@400;500&family=Fraunces:opsz,wght@144,600&display=swap">
<style>
  :root {
    --page-bg: #e9e4dc;
    --cap-black: #171514;
    --peach-light: #fde6cf;
    --peach-mid: #fbc893;
    --peach-edge: #f6b071;
    --ring-white: #ffffff;
    --ink: #1d1b1a;
    --banner-grey: #3b3a3a;
    --syrup-orange: #df5a2c;
    --dog-light: #c9773a;
    --dog-dark: #7a3d17;
    --leaf-light: #f39a3c;
    --leaf-dark: #d4521c;
  }
  html, body {
    margin: 0;
    width: 1200px;
    height: 1200px;
    overflow: hidden;
    background: var(--page-bg);
  }
  .canvas {
    position: relative;
    width: 1200px;
    height: 1200px;
  }
  .label {
    position: absolute;
    left: 100px;
    top: 100px;
    width: 1000px;
    height: 1000px;
  }
  .brand-name {
    font-family: "Lexend", sans-serif;
    font-weight: 400;
    font-size: 58px;
    fill: var(--ring-white);
  }
  .location {
    font-family: "Lexend", sans-serif;
    font-weight: 400;
    font-size: 58px;
    fill: var(--ink);
  }
  .grade-text {
    font-family: "Lexend", sans-serif;
    font-weight: 400;
    font-size: 31px;
    fill: var(--ring-white);
  }
  .product-name {
    font-family: "Fraunces", serif;
    font-weight: 600;
    font-size: 100px;
    fill: var(--syrup-orange);
  }
  .volume {
    font-family: "Lexend", sans-serif;
    font-weight: 400;
    font-size: 27px;
    fill: var(--ink);
  }
</style>
</head>
<body>
<div class="canvas">
  <svg class="label" viewBox="0 0 1000 1000" xmlns="http://www.w3.org/2000/svg">
    <defs>
      <radialGradient id="label-face" cx="50%" cy="42%" r="60%">
        <stop offset="0%" stop-color="var(--peach-light)"/>
        <stop offset="55%" stop-color="var(--peach-mid)"/>
        <stop offset="100%" stop-color="var(--peach-edge)"/>
      </radialGradient>
      <linearGradient id="dog-tone" x1="0" y1="0" x2="1" y2="1">
        <stop offset="0%" stop-color="var(--dog-light)"/>
        <stop offset="100%" stop-color="var(--dog-dark)"/>
      </linearGradient>
      <radialGradient id="leaf-tone" cx="50%" cy="45%" r="55%">
        <stop offset="0%" stop-color="var(--leaf-light)"/>
        <stop offset="100%" stop-color="var(--leaf-dark)"/>
      </radialGradient>
      <clipPath id="label-shape">
        <circle cx="500" cy="500" r="500"/>
      </clipPath>
      <path id="brand-arc" d="M70 500 A430 430 0 0 1 930 500"/>
      <path id="location-arc" d="M125 500 A375 375 0 0 0 875 500"/>
    </defs>

    <g clip-path="url(#label-shape)">
      <rect class="label-face" width="1000" height="1000" fill="url(#label-face)"/>
      <path class="top-cap" d="M0 0 H1000 V290 Q500 140 0 290 Z" fill="var(--cap-black)"/>
    </g>

    <path class="inner-ring" d="M185 185 A445 445 0 0 0 99 693" fill="none" stroke="var(--ring-white)" stroke-width="3"/>
    <path class="inner-ring" d="M815 185 A445 445 0 0 1 901 693" fill="none" stroke="var(--ring-white)" stroke-width="3"/>

    <text class="brand-name" text-anchor="middle">
      <textPath href="#brand-arc" startOffset="50%">Bright Hollow Syrup</textPath>
    </text>

    <rect class="dog-illustration" x="360" y="110" width="255" height="325" rx="110"
          fill="url(#dog-tone)" role="img" aria-label="Illustration of an Irish setter's head, tongue out, facing left"/>

    <g class="grade-banner">
      <path d="M281 460 H712 L697 483 L712 506 H281 L296 483 Z" fill="var(--banner-grey)"/>
      <text class="grade-text" x="496" y="494" text-anchor="middle">★ GRADE A AMBER ★</text>
    </g>

    <text class="product-name" x="500" y="604" text-anchor="middle">MAPLE SYRUP</text>
    <text class="volume" x="500" y="656" text-anchor="middle">8 FL OZ (237 ML)</text>

    <ellipse class="maple-leaf" cx="500" cy="742" rx="66" ry="64"
             fill="url(#leaf-tone)" role="img" aria-label="Illustration of an orange maple leaf"/>

    <text class="location" text-anchor="middle">
      <textPath href="#location-arc" startOffset="50%">Schoodic Lake, Maine</textPath>
    </text>
  </svg>
</div>
</body>
</html>
```